Personal Chef Business Card Design

My company, Simmerly, is a personal in-home chef service that caters to clients' needs, but I am not a caterer. The types of services that I provide range from : weekly menus for busy families, special menus for specific diets, custom menus, private parties, intimate dinners, and brunch parties. My cooking style is seasonal and simple with the option of a variety of cuisines. I like colorful and simple business cards. My business is just getting started as I will be the only employee for now. I would like to be able to use the design on the card for my logo also. I don't know if logo design is a different service altogether.

If you can convince me to go with double-sided, then so be it, but until then, I'll stick with singe-sided.

Target Market(s)

busy families, health conscious, private parties, brunch parties, dinner parties

Industry/Entity Type

Chef

Contact Information for Business Card

Owen Farley
owenfarley@mailbrook.net
571-806-3172
Simmerly Personal Chef Service
Serving the DC/VA/MD area

Font styles to use
Serif
Sans Serif
Decorative
Script
Other font styles liked:
• Anything

Requirements
Must have
• I will be using the illustration as my logo so that I can use it for promotional merchandise.

```html
<!DOCTYPE html>
<html lang="en">
<head>
<meta charset="utf-8">
<title>Simmerly Business Card</title>
<link rel="stylesheet" href="https://fonts.googleapis.com/css2?family=Federo&family=Open+Sans:wght@400;600;700&display=swap">
<style>
  :root {
    --page-bg: #e4e4e2;
    --brand-red: #951a1e;
    --brand-yellow: #ffd673;
    --card-white: #ffffff;
    --card-shadow: rgba(0, 0, 0, 0.18);
  }
  * { box-sizing: border-box; margin: 0; padding: 0; }
  html, body {
    width: 1200px;
    height: 900px;
    overflow: hidden;
  }
  body {
    background: var(--page-bg);
    font-family: "Open Sans", Arial, sans-serif;
    display: flex;
    flex-direction: column;
    align-items: center;
    justify-content: center;
    gap: 56px;
  }
  .card {
    position: relative;
    width: 600px;
    height: 343px;
    background: var(--brand-yellow);
    box-shadow: 0 6px 18px var(--card-shadow);
    overflow: hidden;
  }
  .band {
    position: absolute;
    left: 0;
    width: 100%;
    background: var(--brand-red);
  }
  .card-front .band-top { top: 0; height: 64px; }
  .card-front .band-bottom { bottom: 0; height: 30px; }
  .card-front .brand { left: 170px; top: 140px; }

  .card-back .band-main { top: 126px; height: 186px; }
  .card-back .brand { left: 170px; top: 50px; }

  .brand {
    position: absolute;
    display: flex;
    align-items: center;
    gap: 14px;
  }
  .brand-mark {
    width: 44px;
    height: 44px;
    background: var(--brand-red);
  }
  .brand-name {
    color: var(--brand-red);
    font-family: "Federo", "Open Sans", sans-serif;
    font-weight: 400;
    font-size: 42px;
    letter-spacing: 2px;
    line-height: 1;
  }

  .holder {
    position: absolute;
    left: 30px;
    top: 138px;
    color: var(--card-white);
  }
  .holder-name {
    font-weight: 700;
    font-size: 21px;
    line-height: 1.1;
  }
  .holder-title {
    font-weight: 400;
    font-size: 13px;
    margin-top: 2px;
  }

  .contact-list {
    position: absolute;
    right: 26px;
    top: 208px;
    list-style: none;
    color: var(--card-white);
    font-size: 15px;
    line-height: 22px;
    text-align: right;
  }
  .contact-list li {
    display: flex;
    justify-content: flex-end;
    align-items: center;
    gap: 10px;
  }
  .contact-icon {
    width: 13px;
    height: 13px;
    flex: none;
  }
</style>
</head>
<body>

  <section class="card card-front" aria-label="Card front">
    <div class="band band-top"></div>
    <div class="brand">
      <div class="brand-mark"></div>
      <span class="brand-name">SIMMERLY</span>
    </div>
    <div class="band band-bottom"></div>
  </section>

  <section class="card card-back" aria-label="Card back">
    <div class="brand">
      <div class="brand-mark"></div>
      <span class="brand-name">SIMMERLY</span>
    </div>
    <div class="band band-main"></div>
    <div class="holder">
      <p class="holder-name">Owen Farley</p>
      <p class="holder-title">Personal Chef</p>
    </div>
    <ul class="contact-list">
      <li>571-806-3172
        <svg class="contact-icon" viewBox="0 0 16 16" fill="#fff"><path d="M3 2l3 0 1 3-2 1.5c1 2 2.5 3.5 4.5 4.5L11 9l3 1v3c0 1-1 1.5-2 1.5C6.5 14 2 9.5 1.5 4 1.5 3 2 2 3 2z"/></svg>
      </li>
      <li>owenfarley@mailbrook.net
        <svg class="contact-icon" viewBox="0 0 16 16" fill="#fff"><rect x="1" y="3" width="14" height="10" rx="1"/><path d="M1.5 3.5L8 9l6.5-5.5" stroke="#951a1e" stroke-width="1.3" fill="none"/></svg>
      </li>
      <li>www.simmerlychef.com
        <svg class="contact-icon" viewBox="0 0 16 16" fill="none" stroke="#fff" stroke-width="1.8"><rect x="1.5" y="6" width="7" height="4" rx="2" transform="rotate(-45 5 8)"/><rect x="7.5" y="6" width="7" height="4" rx="2" transform="rotate(-45 11 8)"/></svg>
      </li>
      <li>Serving the DC/VA/MD area
        <svg class="contact-icon" viewBox="0 0 16 16" fill="#fff"><path d="M8 1a5 5 0 0 1 5 5c0 3.5-5 9-5 9S3 9.5 3 6a5 5 0 0 1 5-5z"/><circle cx="8" cy="6" r="2" fill="#951a1e"/></svg>
      </li>
    </ul>
  </section>

</body>
</html>
```